13 Tavo - new website design project

Our company Tavo Electrical is developing a new lead generation website focused on Electrical, LED Lighting and Solar Power. We need a high converting website.

Example of our current website is www.tavoelectrical.com.au You can take content from this website for this new design. Our colours are red, black and white. For our new website we would like to promote Tavo, Bright Days Ahead. Please listen to the jingle.

The below link is the company jingle that we have developed.
http://www.tunecraftaudio.com.au/tav-tc-v1/

The key for this brief is to generate leads for Electrical, LED Lighting (for commercial) and Solar Power & Storage.

Target Market(s)

Business owners in Melbourne Victoria

Number of Pages Required

4 page

Colors
ec1f27
ffffff

Requirements
Must have
• This page must be clean, be in line with company branding and a high converting lead website.

```html
<!DOCTYPE html>
<html lang="en">
<head>
<meta charset="utf-8">
<title>Tavo Electrical</title>
<link href="https://fonts.googleapis.com/css2?family=Open+Sans:wght@300;400;600;700&display=swap" rel="stylesheet">
<style>
:root{
  --red:#ec1f27;
  --white:#ffffff;
  --ink:#222222;
  --text:#6d6d6d;
  --dark:#232323;
  --darker:#1c1c1c;
  --tabbar:#2b2b2b;
  --line:#e6e6e6;
  --muted:#8f8f8f;
}
*{box-sizing:border-box;margin:0;padding:0}
html,body{width:1200px;height:2466px;overflow:hidden}
body{font-family:"Open Sans",Arial,sans-serif;background:var(--white);color:var(--ink);position:relative}
.abs{position:absolute}

/* header */
.site-header{position:absolute;top:0;left:0;width:1200px;height:53px;background:var(--white);z-index:2}
.brand{position:absolute;left:145px;top:9px;display:flex;align-items:center;gap:10px;font-weight:700;font-size:26px;color:var(--ink);letter-spacing:1px}
.brand-mark{width:22px;height:22px;border-radius:50%;background:var(--red)}
.main-nav{position:absolute;left:370px;top:16px;display:flex;gap:36px;font-size:15px;color:#444;letter-spacing:1px}

/* hero */
.hero{position:absolute;top:53px;left:0;width:1200px;height:657px;
  background:linear-gradient(180deg,#7fa6c9 0%,#a9c0d6 28%,#8a7a6a 55%,#5b3a2c 80%,#3d2a22 100%)}
.hero-title{position:absolute;top:135px;width:100%;text-align:center;color:var(--white);font-weight:300;font-size:64px;line-height:71px;letter-spacing:6px}
.hero-sub{position:absolute;top:344px;width:100%;text-align:center;color:var(--red);font-weight:700;font-size:19px;line-height:26px;letter-spacing:6px}
.hero-band{position:absolute;top:597px;left:0;width:100%;height:57px;background:rgba(20,20,20,.55);color:var(--white);text-align:center;font-size:16px;font-weight:600;letter-spacing:5px;line-height:57px}

/* intro */
.section-title{font-size:20px;font-weight:600;color:var(--ink)}
.title-rule{width:41px;height:3px;background:var(--red);margin-top:14px}
.why{position:absolute;left:94px;top:795px;width:450px}
.why-item{margin-top:18px}
.why-item:first-of-type{margin-top:24px}
.why-item h3{font-size:17px;font-weight:400;color:var(--ink);display:flex;align-items:center;gap:6px}
.why-item p{font-size:12.5px;line-height:25px;color:var(--text);margin-top:6px}
.about{position:absolute;left:613px;top:795px;width:497px}
.about-photo{float:left;width:270px;height:161px;margin:24px 16px 4px 0;
  background:linear-gradient(135deg,#e9e9e9 0%,#9aa0a6 45%,#3d4450 100%)}
.about p{font-size:12.5px;line-height:25px;color:var(--text);padding-top:22px}
.partners{position:absolute;left:613px;top:1151px;width:497px;height:151px;display:grid;grid-template-columns:repeat(3,1fr);grid-template-rows:1fr 1fr}
.partner{display:flex;align-items:center;justify-content:center;border-right:1px solid var(--line);font-size:17px;font-weight:600;color:var(--red)}
.partner:nth-child(3n){border-right:none}
.partner:nth-child(-n+3){border-bottom:1px solid var(--line)}

/* services tabs */
.tabs{position:absolute;top:1422px;left:0;width:1200px;height:66px;background:var(--tabbar);border-top:1px solid #3a3a3a;border-bottom:1px solid #3a3a3a}
.tab{position:absolute;top:0;height:64px;line-height:64px;font-size:20px;font-weight:600;color:var(--white)}
.tab.active{color:var(--red)}
.tab-divider{position:absolute;top:0;width:1px;height:64px;background:#444}
.service{position:absolute;top:1488px;left:0;width:1200px;height:342px;background:var(--dark)}
.service-photo{position:absolute;left:94px;top:44px;width:406px;height:247px;
  background:linear-gradient(160deg,#d7dbe0 0%,#7b8795 45%,#e06c2c 78%,#c9d63a 100%)}
.service-body{position:absolute;left:526px;top:54px;width:590px}
.service-body h2{font-size:18px;font-weight:600;color:var(--white)}
.service-body p{font-size:12px;line-height:22px;color:var(--muted);margin-top:10px}

/* experience */
.experience{position:absolute;top:1830px;left:0;width:1200px;height:513px;
  background:linear-gradient(120deg,#3b4a5c 0%,#5a6470 35%,#4a3e36 65%,#2a2e33 100%)}
.exp-title{position:absolute;top:96px;width:100%;text-align:center;color:var(--white);font-size:33px;font-weight:400}
.exp-icon{position:absolute;top:180px;width:120px;text-align:center;color:var(--white);font-size:13px;font-weight:700}
.exp-icon svg{display:block;margin:0 auto 10px;width:60px;height:64px;fill:var(--white)}
.exp-tag{position:absolute;top:310px;width:100%;text-align:center;color:var(--white);font-size:25px}
.btn{position:absolute;left:529px;top:384px;width:142px;height:42px;background:var(--red);color:var(--white);font-size:14px;line-height:42px;text-align:center}

/* testimonial */
.testimonial{position:absolute;top:2343px;left:0;width:1200px;height:123px;background:var(--darker)}
.testimonial-photo{position:absolute;left:291px;top:28px;width:54px;height:49px;background:linear-gradient(180deg,#c9c9c9,#6f6a63)}
.testimonial-name{position:absolute;left:362px;top:26px;color:var(--white);font-size:14px;font-weight:600}
.testimonial-quote{position:absolute;left:362px;top:55px;width:520px;color:var(--white);font-size:12.5px;line-height:25px}
</style>
</head>
<body>

<header class="site-header">
  <div class="brand"><span class="brand-mark"></span>TAVO</div>
  <nav class="main-nav"><span>HOME</span><span>TAVO STORY</span><span>OUR WORK</span><span>CAREERS</span><span>CONTACT US</span></nav>
</header>

<section class="hero" role="img" aria-label="Photo of electricians installing solar panels on a brick wall">
  <h1 class="hero-title">WELCOME TO<br>TAVO ELECTRICAL</h1>
  <p class="hero-sub">THE HOME OF SPECIALISTS IN<br>ELECTRICAL, LED LIGHTING AND SOLAR POWER</p>
  <div class="hero-band">AUSTRALIA'S LARGEST FULLY INTEGRATED ELECTRICAL &amp; ENERGY SOLUTIONS PROVIDER</div>
</section>

<section class="why">
  <h2 class="section-title">Why Choose Us?</h2>
  <div class="title-rule"></div>
  <div class="why-item"><h3><svg width="10" height="14" viewBox="0 0 10 14"><path d="M5 1a4 4 0 0 0-4 4c0 3 4 8 4 8s4-5 4-8a4 4 0 0 0-4-4z" fill="none" stroke="#ec1f27" stroke-width="1.6"/></svg>Professional Service</h3>
    <p>When you hire a Tavo Electrical Electrician you will get a professional and well-presented Electrician that comes skilled and ready to do the job.</p></div>
  <div class="why-item"><h3><svg width="10" height="14" viewBox="0 0 10 14"><path d="M5 1a4 4 0 0 0-4 4c0 3 4 8 4 8s4-5 4-8a4 4 0 0 0-4-4z" fill="none" stroke="#ec1f27" stroke-width="1.6"/></svg>5 Year Workmanship Guarantee</h3>
    <p>You can buy with confidence as all of our work has a 5 year workmanship guarantee. For your peace of mind, we unconditionally back our electrical work. We will come back to fix any problems at our own expense.</p></div>
  <div class="why-item"><h3><svg width="10" height="14" viewBox="0 0 10 14"><path d="M5 1a4 4 0 0 0-4 4c0 3 4 8 4 8s4-5 4-8a4 4 0 0 0-4-4z" fill="none" stroke="#ec1f27" stroke-width="1.6"/></svg>Value For Money</h3>
    <p>We provide extremely competitive pricing, which means you get value for money on quality that is comparable to the best in the industry.</p></div>
  <div class="why-item"><h3><svg width="10" height="14" viewBox="0 0 10 14"><path d="M5 1a4 4 0 0 0-4 4c0 3 4 8 4 8s4-5 4-8a4 4 0 0 0-4-4z" fill="none" stroke="#ec1f27" stroke-width="1.6"/></svg>Environmentally Friendly</h3>
    <p>We a committed to reducing carbon emissions by installing Solar Power and upgrading sites to LED Lighting. In addition to reducing the carbon emissions we recycle Fluorescent Tubes, Highbay Globes, Metal and Cardboard.</p></div>
  <div class="why-item"><h3><svg width="10" height="14" viewBox="0 0 10 14"><path d="M5 1a4 4 0 0 0-4 4c0 3 4 8 4 8s4-5 4-8a4 4 0 0 0-4-4z" fill="none" stroke="#ec1f27" stroke-width="1.6"/></svg>Fully Insured</h3>
    <p>Tavo Electrical is fully insured and equipped to handle break downs and service call outs.</p></div>
</section>

<section class="about">
  <h2 class="section-title">About Us</h2>
  <div class="title-rule"></div>
  <div class="about-photo" role="img" aria-label="Photo of an electrician testing a switchboard with a multimeter"></div>
  <p>Tavo Electrical was formed to be an expert Electricity Contracting Company providing services to all Residential and Commercial Customers. With over 10 years of experience, Tavo Electrical has developed a highly-experienced team of professionals that ensure all our customer expectations are met. Electrical and Energy Solutions are at the forefront of our company. Tavo Electrical has a long history in Electrical, LED Lighting and Solar Power and just like the Cougar.</p>
</section>

<div class="partners">
  <div class="partner">Lumora</div>
  <div class="partner">Heron Plumbing</div>
  <div class="partner">Lumora</div>
  <div class="partner">Outback Surplus</div>
  <div class="partner">Golden Grill</div>
  <div class="partner">Outback Surplus</div>
</div>

<nav class="tabs">
  <span class="tab active" style="left:123px">Industrial</span>
  <span class="tab-divider" style="left:247px"></span>
  <span class="tab" style="left:278px">Domestic</span>
  <span class="tab-divider" style="left:397px"></span>
  <span class="tab" style="left:431px">Testing and Inspection</span>
  <span class="tab-divider" style="left:674px"></span>
  <span class="tab" style="left:708px">Solar Power</span>
  <span class="tab-divider" style="left:853px"></span>
  <span class="tab" style="left:885px">Security Systems</span>
</nav>

<section class="service">
  <div class="service-photo" role="img" aria-label="Photo of two workers in hi-vis gear beside an industrial transformer"></div>
  <div class="service-body">
    <h2>Lorem Ipsum Laudantium Consetetur Sadipscing</h2>
    <p>Sed ut perspiciatis unde omnis iste natus error sit voluptatem accusantium doloremque laudantium, totam rem aperiam, eaque ipsa quae ab illo inventore veritatis et quasi architecto beatae vitae dicta sunt explicabo. Nemo enim ipsam voluptatem quia laudantium totam rem. Stet clita kasd gubergren, no sea takimata sanctus est Lorem ipsum dolor sit amet.</p>
    <p>Lorem ipsum dolor sit amet consetetur sadipscing elitr sed diam nonumy eirmod tempor invidunt ut labore et dolore magna aliquyam erat sed diam voluptua. Nemo enim ipsam voluptatem quia voluptas sit aspernatur aut odit aut fugit, sed quia consequuntur magni dolores eos qui ratione voluptatem sequi nesciunt. Sed ut perspiciatis unde omnis iste natus error sit voluptatem accusantium laudantium totam rem aperiam eaque ipsa.</p>
  </div>
</section>

<section class="experience" role="img" aria-label="Photo of an electrician in a hard hat working on a switchboard">
  <h2 class="exp-title">OVER 30 YEARS SPECIALIST EXPERIENCE</h2>
  <div class="exp-icon" style="left:272px"><svg viewBox="0 0 60 64"><rect x="18" y="2" width="5" height="16"/><rect x="37" y="2" width="5" height="16"/><path d="M10 18h40v14a20 20 0 0 1-17 19v11h-6V51A20 20 0 0 1 10 32z"/></svg>DOMESTIC</div>
  <div class="exp-icon" style="left:397px"><svg viewBox="0 0 60 64"><path d="M8 62V26l14-8v8l14-8v8l14-8V4h6v58z"/><rect x="14" y="36" width="6" height="6" fill="#4a4a4a"/><rect x="26" y="36" width="6" height="6" fill="#4a4a4a"/><rect x="38" y="36" width="6" height="6" fill="#4a4a4a"/><rect x="26" y="48" width="8" height="14" fill="#4a4a4a"/></svg>INDUSTRIAL</div>
  <div class="exp-icon" style="left:527px"><svg viewBox="0 0 60 64"><path d="M30 2l-8 14H8v4h13l-5 12H12v4h3L8 62h6l16-22 16 22h6l-7-26h3v-4h-4l-5-12h13v-4H38zm0 8l5 6H25zm-6 10h12l4 12H20zm6 16l9 0-9 14-9-14z"/></svg>CONTRACTOR</div>
  <div class="exp-icon" style="left:673px"><svg viewBox="0 0 60 64"><path d="M4 6h52v38H34v8h10v4H16v-4h10v-8H4zm5 5v28h42V11z"/><path d="M11 26h10l4-9 6 16 4-9h14" fill="none" stroke="#fff" stroke-width="3"/></svg>ANALYSIS</div>
  <div class="exp-icon" style="left:806px"><svg viewBox="0 0 60 64"><path d="M12 24a18 18 0 0 1 36 0h4v5H8v-5z"/><rect x="27" y="4" width="6" height="10"/><path d="M16 33h28v6H16z"/><path d="M6 62c0-12 10-18 24-18s24 6 24 18z"/></svg>QUALIFIED</div>
  <p class="exp-tag">Quality Reliable Service at Affordable Prices</p>
  <span class="btn">CONTACT US</span>
</section>

<section class="testimonial">
  <div class="testimonial-photo" role="img" aria-label="Small photo of a completed job"></div>
  <p class="testimonial-name">R. Delmar Balwyn – North VIC</p>
  <p class="testimonial-quote">They clean up after the job, explained everything I needed to know and answered all questions, very professional. Will use them again in the future!</p>
</section>

</body>
</html>
```